Label for Olive Oil Bottle SOMVETTA

Dear Designers,
The task is to create a label for an Olive Oil Bottle for the Somvetta Brand.
Please see the attached files for the information that must appear on the label.
Please produce the label in three different colour schemes: Red for the MERVO version of the label,
Blue for the SELTA version and light green for the DORVANTE version of the label.
Please present the label on photorealistic bottle bock-ups like shown in the file attached.
It is not necessary to use the same template but it must be similar.

Target Market(s)

Germany, Austria and Swizerland

Industry/Entity Type

Food Production

Font styles to use
Serif
Script

Requirements
Must have
• a) Please produce 3 different versions of the label:
• 1. MERVO
• 2. SELTA
• 3. DORVANTE
• b) Please use for the presentation of the labels the bottles in the attached file.
• They are in big scale so feel free to scale them down
• c) Please present the label on a white/transparent background
• d) Please fint the information for the labels on the files attached
Nice to have
• - Please see the file example.pdf to have a ROUGH idea how the design COULD be.
• - The label/mockup should be presented on a white/transparent background
Should not have
• Ill tell you...

```html
<!DOCTYPE html>
<html lang="de">
<head>
<meta charset="utf-8">
<title>Somvetta Mervo – Olivenöl Etikett</title>
<link rel="stylesheet" href="https://fonts.googleapis.com/css2?family=Cinzel:wght@400;700&family=Dancing+Script:wght@700&display=block">
<style>
  :root {
    --label-red: #e31b23;
    --deep-red: #c8102e;
    --gold-light: #f3e2a8;
    --gold: #c9a24a;
    --gold-dark: #8a6a22;
    --sky: #e3eef7;
    --white: #ffffff;
    --olive-light: #c7d35a;
    --olive-mid: #8fb048;
    --ink-brown: #4a3a1a;
  }
  html, body {
    margin: 0;
    padding: 0;
    width: 1200px;
    height: 1200px;
    overflow: hidden;
    background: var(--white);
  }
  .canvas {
    position: relative;
    width: 1200px;
    height: 1200px;
  }
  .label {
    position: absolute;
    left: 300px;
    top: 40px;
    width: 600px;
    height: 1120px;
  }
  .label-shape {
    position: absolute;
    inset: 0;
    width: 100%;
    height: 100%;
  }
  .label-text {
    position: absolute;
    left: 0;
    width: 100%;
    text-align: center;
    font-family: "Cinzel", serif;
    line-height: 1;
    margin: 0;
  }
  .brand-name {
    top: 132px;
    font-size: 40px;
    font-weight: 700;
    letter-spacing: 2px;
    color: var(--deep-red);
  }
  .variant-name {
    top: 196px;
    font-family: "Dancing Script", cursive;
    font-weight: 700;
    font-size: 116px;
    color: var(--label-red);
  }
  .olive-art {
    position: absolute;
    left: 80px;
    top: 332px;
    width: 440px;
    height: 338px;
    border-radius: 48%;
    background: radial-gradient(ellipse at 50% 50%, var(--olive-light) 0%, var(--olive-mid) 45%, rgba(63,122,42,0.35) 75%, rgba(227,238,247,0) 100%);
  }
  .product-line-1 {
    top: 682px;
    font-size: 76px;
    color: var(--deep-red);
  }
  .product-line-2 {
    top: 750px;
    font-size: 52px;
    color: var(--deep-red);
  }
  .ribbon-text {
    top: 831px;
    font-size: 21px;
    color: var(--white);
    letter-spacing: 1px;
  }
  .temperature {
    top: 880px;
    font-size: 21px;
    color: var(--deep-red);
  }
  .origin {
    top: 924px;
    font-size: 20px;
    line-height: 25px;
    color: var(--ink-brown);
    letter-spacing: 0.5px;
  }
  .volume {
    position: absolute;
    left: 253px;
    top: 1018px;
    width: 94px;
    height: 32px;
    border-radius: 16px;
    background: var(--label-red);
    color: var(--white);
    font-family: "Cinzel", serif;
    font-weight: 700;
    font-size: 20px;
    line-height: 32px;
    text-align: center;
  }
</style>
</head>
<body>
<main class="canvas">
  <section class="label">
    <svg class="label-shape" viewBox="0 0 680 1270" preserveAspectRatio="none" xmlns="http://www.w3.org/2000/svg" aria-hidden="true">
      <defs>
        <path id="label-outline" d="M340,0 C430,0 500,40 520,110 C600,120 670,170 675,260 L680,900 C680,1110 530,1270 340,1270 C150,1270 0,1110 0,900 L5,260 C10,170 80,120 160,110 C180,40 250,0 340,0 Z"/>
        <pattern id="stripe-field" width="20" height="16" patternUnits="userSpaceOnUse">
          <rect width="20" height="16" fill="#e3eef7"/>
          <rect y="11" width="20" height="5" fill="#ffffff"/>
        </pattern>
        <linearGradient id="gold-band" x1="0" y1="0" x2="1" y2="0">
          <stop offset="0" stop-color="#c9a24a"/>
          <stop offset="0.5" stop-color="#f3e2a8"/>
          <stop offset="1" stop-color="#c9a24a"/>
        </linearGradient>
        <linearGradient id="gold-frame" x1="0" y1="0" x2="0" y2="1">
          <stop offset="0" stop-color="#f3e2a8"/>
          <stop offset="0.5" stop-color="#c9a24a"/>
          <stop offset="1" stop-color="#8a6a22"/>
        </linearGradient>
        <clipPath id="inner-clip">
          <use href="#label-outline" transform="translate(340 635) scale(0.9) translate(-340 -635)"/>
        </clipPath>
      </defs>
      <use class="outer-border" href="#label-outline" fill="#e31b23"/>
      <use class="white-margin" href="#label-outline" fill="#ffffff" transform="translate(340 635) scale(0.955) translate(-340 -635)"/>
      <use class="gold-frame" href="#label-outline" fill="none" stroke="url(#gold-frame)" stroke-width="7" transform="translate(340 635) scale(0.915) translate(-340 -635)"/>
      <g clip-path="url(#inner-clip)">
        <rect class="stripe-field" x="0" y="0" width="680" height="1270" fill="url(#stripe-field)"/>
        <rect class="lower-white" x="0" y="1130" width="680" height="140" fill="#ffffff"/>
        <rect class="origin-band" x="0" y="1040" width="680" height="96" fill="url(#gold-band)"/>
      </g>
      <g class="ribbon">
        <polygon points="140,950 205,942 205,1000 140,1012 168,978" fill="#c8102e"/>
        <polygon points="540,950 475,942 475,1000 540,1012 512,978" fill="#c8102e"/>
        <rect x="195" y="925" width="290" height="62" fill="#e31b23"/>
      </g>
    </svg>

    <p class="label-text brand-name">SOMVETTA</p>
    <p class="label-text variant-name">Mervo</p>
    <div class="olive-art" role="img" aria-label="Illustration eines Olivenzweigs mit grünen Oliven und Blättern"></div>
    <p class="label-text product-line-1">OLIO DI</p>
    <p class="label-text product-line-2">OLIVA</p>
    <p class="label-text ribbon-text">IDEAL ZUM BRATEN</p>
    <p class="label-text temperature">BIS 220°C</p>
    <p class="label-text origin">NATIVES OLIVENÖL EXTRA -<br>AUS DER EUROPÄISCHEN<br>UNION</p>
    <div class="volume">750ML</div>
  </section>
</main>
</body>
</html>
```